website refresh/redesign needed for Printing e commerce website

We'd like a website refresh/redesign done with the specific goal of having the site act as a more effective funnel for leads.<br/><br/>We think that the current design is outdated.<br/><br/>We want our customers and partners to still recognize the website, Is a big chunk of our business is repeat orders. <br/>so it should not be a full redesign. General color scheme and such should remain the same so that it is clear we are the same company. <br/><br/>However, the updated website design should look more polished and convey high-quality products and services that we provide. <br/><br/>Our website is https://shopledgerformsnet.quillpaperdepot.com/ if you want to take a look at our current website design. <br/><br/>we need 3 pages redesigned... <br/><br/>1. homepage:https://shopledgerformsnet.quillpaperdepot.com/<br/><br/>2. Category page: <br/>https://shopledgerformsnet.quillpaperdepot.com/order-computer-checks-c-4.html<br/><br/>3. Product detail page: https://shopledgerformsnet.quillpaperdepot.com/voucher-computer-checks-p-35.html<br/><br/> I can provide many more pictures of our products if needed.<br/><br/><br/>BTW. I have another project here on brief bazaar, you can check the other ones too, so to make it easier to do both when working on this.<br/><br/> Please reach out to me should you have any questions or comments.

```html
<!DOCTYPE html>
<html lang="en">
<head>
<meta charset="utf-8">
<title>Shop Ledger Forms – Computer Checks</title>
<link rel="stylesheet" href="https://fonts.googleapis.com/css2?family=Sarabun:wght@300;400;600;700&display=swap">
<style>
  :root{
    --green:#8fe77c;
    --green-soft:#e0f7da;
    --green-dark:#1b3a10;
    --ink:#111;
    --muted:#9a9a9a;
    --card:#fff;
    --shadow:0 6px 22px rgba(0,0,0,.08);
  }
  *{box-sizing:border-box;margin:0;padding:0}
  html,body{width:1069px;height:1200px;overflow:hidden;background:#fff;font-family:"Sarabun",sans-serif;color:var(--ink)}
  .page{position:relative;width:1069px;height:1200px}
  .abs{position:absolute}
  .user-icon{left:40px;top:36px}
  .cart-icon{left:1012px;top:33px}
  .brand{left:392px;top:24px;width:283px;height:42px;border-radius:21px;background:#fff;box-shadow:var(--shadow);display:flex;align-items:center;justify-content:center;gap:8px;font-weight:700;font-size:19px;color:var(--green-dark)}
  .brand-dot{width:9px;height:9px;border-radius:50%;background:var(--green)}
  .main-nav{left:0;top:84px;width:1069px;display:flex;justify-content:center;gap:36px;font-size:11px;align-items:center}
  .main-nav a{color:var(--ink);text-decoration:none}
  .main-nav a.active{text-decoration:underline}
  .steps{left:285px;top:180px;display:flex;align-items:center}
  .step{width:60px;height:60px;border-radius:50%;background:var(--green-soft);color:#fff;font-size:34px;font-weight:600;display:flex;align-items:center;justify-content:center;box-shadow:var(--shadow)}
  .step.current{background:var(--green)}
  .step-dots{display:flex;gap:12px;margin:0 21px}
  .step-dots i{width:10px;height:10px;border-radius:50%;background:#eee}
  .step-label{left:235px;top:246px;width:160px;text-align:center;font-size:22px;font-weight:400}
  .config-panel{left:40px;top:342px;width:273px;height:724px;background:var(--card);border-radius:22px;box-shadow:var(--shadow)}
  .product-title{left:40px;top:362px;width:273px;text-align:center;font-size:25px;font-weight:400}
  .product-price{left:40px;top:400px;width:273px;text-align:center;font-size:12px;font-weight:700}
  .option-card{background:var(--card);border-radius:18px;box-shadow:var(--shadow);width:203px;left:75px}
  .option-title{position:absolute;left:0;width:100%;text-align:center;font-size:10.5px}
  .swatch-row{position:absolute;left:0;width:100%;display:flex;justify-content:center;gap:8px}
  .swatch{width:34px;height:40px;display:flex;flex-direction:column;border:1px solid #ccc}
  .swatch span{flex:1;border-bottom:1px solid #bbb}
  .swatch span:last-child{border-bottom:none}
  .swatch-wrap{width:52px;height:56px;display:flex;align-items:center;justify-content:center;border-radius:10px;border:1.5px solid transparent}
  .swatch-wrap.selected{border-color:var(--green)}
  .layout-list{position:absolute;left:0;top:50px;width:100%;text-align:center}
  .layout-list div{color:#666}
  .layout-list .far{font-size:10px;color:#bbb;height:16px;line-height:16px}
  .layout-list .near{font-size:12px;height:19px;line-height:19px}
  .layout-list .chosen{font-size:14px;color:var(--ink);margin:0 24px;height:26px;line-height:23px;border:1.5px solid var(--green);border-radius:13px}
  .scroll-track{position:absolute;right:5px;top:57px;width:1px;height:70px;background:#ccc}
  .scroll-thumb{position:absolute;right:3px;top:71px;width:5px;height:14px;border-radius:3px;background:var(--green)}
  .placeholder{position:absolute;left:0;top:33px;width:100%;text-align:center;font-size:10px;color:#ddd}
  .more-btn{left:126px;top:1015px;width:100px;height:28px;border-radius:14px;background:#fff;box-shadow:var(--shadow);font-size:11px;display:flex;align-items:center;justify-content:center}
  .check-preview{left:347px;top:338px;width:684px;height:725px;background:linear-gradient(90deg,#f6f7fd 0 32%,#fff 32% 33%,#c9d4f0 34%,#dfe6f8 70%,#c7d1ef 100%);border:1px solid #e6e9f5}
  .add-cart{left:473px;top:1121px;width:123px;height:34px;border-radius:17px;background:var(--green-dark);color:#fff;font-size:16px;font-weight:700;display:flex;align-items:center;justify-content:center}
</style>
</head>
<body>
<div class="page">
  <svg class="abs user-icon" width="15" height="17" viewBox="0 0 15 17" aria-label="Account"><circle cx="7.5" cy="4.5" r="4" fill="#1b3a10"/><path d="M0 17c0-5 3-7.5 7.5-7.5S15 12 15 17z" fill="#1b3a10"/></svg>
  <svg class="abs cart-icon" width="22" height="22" viewBox="0 0 22 22" aria-label="Cart"><path d="M2 8h16l-2 8H4z" fill="none" stroke="#1b3a10" stroke-width="1.5"/><path d="M6 8l4-6 4 6" fill="none" stroke="#1b3a10" stroke-width="1.2"/><circle cx="17" cy="17" r="4" fill="#fff" stroke="#1b3a10"/><text x="17" y="19.5" font-size="6" text-anchor="middle" fill="#1b3a10">5</text></svg>

  <div class="abs brand"><span class="brand-dot"></span>Shop Ledger Forms</div>

  <nav class="abs main-nav">
    <a href="#">Business Checks</a>
    <a href="#" class="active">Computer Checks</a>
    <a href="#">LedgerPro Check</a>
    <a href="#">Accessories</a>
    <a href="#">Help</a>
    <a href="#">Re-Order</a>
    <svg width="13" height="14" viewBox="0 0 13 14" aria-label="Search"><circle cx="5.5" cy="5.5" r="4.5" fill="none" stroke="#222"/><path d="M9 9l3.5 4" stroke="#222"/></svg>
  </nav>

  <div class="abs steps">
    <div class="step current">1</div>
    <div class="step-dots"><i></i><i></i><i></i></div>
    <div class="step">2</div>
    <div class="step-dots"><i></i><i></i><i></i></div>
    <div class="step">3</div>
    <div class="step-dots"><i></i><i></i><i></i></div>
    <div class="step">4</div>
  </div>
  <div class="abs step-label">Type/Layout</div>

  <div class="abs config-panel"></div>
  <div class="abs product-title">Computer Checks</div>
  <div class="abs product-price">$15.50</div>

  <div class="abs option-card" style="top:432px;height:103px">
    <div class="option-title" style="top:12px">Select Check Type</div>
    <div class="swatch-row" style="top:37px">
      <div class="swatch-wrap selected"><div class="swatch"><span style="background:#1b3a10"></span><span></span><span></span></div></div>
      <div class="swatch-wrap"><div class="swatch"><span></span><span style="background:#a3b3a0"></span><span></span></div></div>
      <div class="swatch-wrap"><div class="swatch"><span></span><span></span><span style="background:#a3b3a0"></span></div></div>
    </div>
  </div>

  <div class="abs option-card" style="top:557px;height:150px">
    <div class="option-title" style="top:14px">Select Check Layout</div>
    <div class="layout-list">
      <div class="far">Layout 1</div>
      <div class="near">Layout 2</div>
      <div class="chosen">Layout 3</div>
      <div class="near">Layout 4</div>
      <div class="far">Layout 5</div>
    </div>
    <div class="scroll-track"></div><div class="scroll-thumb"></div>
  </div>

  <div class="abs option-card" style="top:727px;height:50px">
    <div class="option-title" style="top:8px">Enter Software and Year</div>
    <div class="placeholder">E.g. TallyBooks 2019</div>
  </div>

  <div class="abs option-card" style="top:800px;height:194px">
    <div class="option-title" style="top:10px">Select Color</div>
    <div class="swatch-row" style="top:36px">
      <div class="swatch-wrap selected"><div class="swatch" style="background:#dff8fb"><span></span><span></span><span></span></div></div>
      <div class="swatch-wrap"><div class="swatch" style="background:#e3f4d6;border-color:#dde"><span></span><span></span><span></span></div></div>
      <div class="swatch-wrap"><div class="swatch" style="background:#fadcde;border-color:#dde"><span></span><span></span><span></span></div></div>
    </div>
    <div class="swatch-row" style="top:106px">
      <div class="swatch-wrap"><div class="swatch" style="background:#d9e5f7;border-color:#dde"><span></span><span></span><span></span></div></div>
      <div class="swatch-wrap"><div class="swatch" style="background:#f8f6d4;border-color:#dde"><span></span><span></span><span></span></div></div>
      <div class="swatch-wrap"><div class="swatch" style="background:#f2def5;border-color:#dde"><span></span><span></span><span></span></div></div>
    </div>
  </div>

  <div class="abs more-btn">More</div>

  <div class="abs check-preview" role="img" aria-label="Preview sheet of three blue security computer checks with ledger stubs"></div>

  <div class="abs add-cart">Add to Cart</div>
</div>
</body>
</html>
```